Flyer Design

I need a flyer as Iam starting a business which cleans Leather couches,sofas,chairs for residential and businesses.
We clean the interiors of automobiles and marine craft, boats large and small.
We would like to be able to get across the message that we are affordable, personal and reliable.
The Gold coast is our market and within this area there is a large amount of holiday apartments and houses which do experience high traffic to their living and dinning areas.

Target Market(s)

Target market Home,Apartment,Marine and Auto Owners

Industry/Entity Type

Residential

Requirements
Must have
• The flyer must have Company name which is BRIGHT HIDE CARE MOBILE NUMBER
0471932054
EMAIL marvtolk@quellnet.com
Colours would like bright Gold or green or Red eith black lettering very modern font
Nice to have
• I would like to keep it as simple and clean looking.but eye catching
Should not have
• Dont want the flyer to look like a Real Estate flyer or a pizza advertisement.

```html
<!DOCTYPE html>
<html lang="en">
<head>
<meta charset="UTF-8">
<title>Bright Hide Care – Flyer</title>
<link href="https://fonts.googleapis.com/css2?family=Oswald:wght@600&family=Exo+2:wght@500;600&display=swap" rel="stylesheet">
<style>
  :root{
    --red:#ec1c24;
    --pink:#f7d0d3;
    --ink:#222;
    --white:#fff;
    --page:#ececec;
  }
  *{margin:0;padding:0;box-sizing:border-box}
  html,body{width:1200px;height:1135px;overflow:hidden;background:var(--page)}
  .flyer{
    position:absolute;left:180px;top:27px;width:840px;height:1080px;
    background:var(--white);border:3px solid var(--red);overflow:hidden;
    font-family:"Exo 2",sans-serif;
  }
  .hero-photo{
    position:absolute;left:0;top:0;width:840px;height:470px;
    background:linear-gradient(180deg,#f3eee8 0%,#eee6dc 38%,#f6f3ee 55%,#ece4d9 78%,#d8c3a6 100%);
  }
  .title-band{
    position:absolute;left:244px;top:30px;width:596px;height:104px;
    background:rgba(255,255,255,.6);
  }
  .brand-name{
    position:absolute;right:33px;top:18px;
    font-family:"Oswald",sans-serif;font-weight:600;font-size:60px;
    color:var(--red);line-height:1;letter-spacing:.3px;
  }
  .wave{position:absolute;left:0;top:0;width:840px;height:700px}
  .headline{
    position:absolute;left:0;top:558px;width:840px;padding-left:70px;text-align:center;line-height:1;
  }
  .headline .lead{display:block;color:var(--red);font-weight:600;font-size:47px}
  .headline .sub{display:block;color:var(--ink);font-weight:600;font-size:34px;margin-top:6px}
  .services{position:absolute;left:33px;top:680px}
  .service{position:absolute;top:0;width:176px}
  .service .shot{height:166px;border:3px solid var(--white);outline:1px solid #ccc}
  .service .caption{
    height:36px;margin-top:7px;background:var(--red);color:var(--white);
    font-weight:600;font-size:17px;display:flex;align-items:center;justify-content:center;
  }
  .shot.carpet{background:linear-gradient(160deg,#e9ecef,#a9aeb3)}
  .shot.sofa{background:linear-gradient(160deg,#d9c9a8,#a68a5e)}
  .shot.chair{background:linear-gradient(160deg,#9a9c9c,#3a4a6a)}
  .shot.auto{background:linear-gradient(160deg,#6f7378,#2b2f35)}
  .tagline{
    position:absolute;left:0;top:932px;width:840px;padding-left:40px;text-align:center;
    font-weight:500;font-size:26px;color:var(--ink);
  }
  .contact{position:absolute;left:12px;top:1000px;width:828px;height:58px;display:flex;gap:5px}
  .contact div{
    background:var(--red);color:var(--white);font-weight:500;font-size:25px;
    display:flex;align-items:center;justify-content:center;
  }
  .contact .phone{width:390px}
  .contact .email{flex:1}
</style>
</head>
<body>
  <main class="flyer">
    <div class="hero-photo" role="img" aria-label="Photo of a woman relaxing on a clean white leather sofa in a bright living room"></div>

    <div class="title-band">
      <h1 class="brand-name">BRIGHT HIDE CARE</h1>
    </div>

    <svg class="wave" viewBox="0 0 840 700" aria-hidden="true">
      <path fill="#f7d0d3" d="M0 454 C60 420 100 400 200 398 C380 396 520 445 660 430 C760 420 830 370 840 300 L840 360 C820 440 740 505 560 512 C400 518 280 505 180 520 C90 535 30 580 0 630 Z"/>
      <path fill="#ec1c24" d="M0 454 C60 420 100 400 200 398 C380 396 520 445 660 430 C760 420 830 370 840 300 L840 350 C820 420 740 480 560 488 C400 494 300 470 200 484 C110 496 40 530 0 580 Z"/>
      <path fill="#fff" d="M840 360 C820 440 740 505 560 512 C400 518 280 505 180 520 C90 535 30 580 0 630 L0 700 L840 700 Z"/>
    </svg>

    <h2 class="headline">
      <span class="lead">Cleaning Services for</span>
      <span class="sub">Residential and Businesses</span>
    </h2>

    <section class="services">
      <div class="service" style="left:0">
        <div class="shot carpet" role="img" aria-label="Photo of a carpet being cleaned with a vacuum machine"></div>
        <div class="caption">Carpets &amp; Rugs</div>
      </div>
      <div class="service" style="left:200px">
        <div class="shot sofa" role="img" aria-label="Photo of a technician cleaning a leather sofa"></div>
        <div class="caption">Leather Sofas</div>
      </div>
      <div class="service" style="left:399px">
        <div class="shot chair" role="img" aria-label="Photo of an office chair being vacuumed"></div>
        <div class="caption">Chairs</div>
      </div>
      <div class="service" style="left:601px">
        <div class="shot auto" role="img" aria-label="Photo of a worker cleaning a vehicle interior"></div>
        <div class="caption">Auto &amp; Marine</div>
      </div>
    </section>

    <p class="tagline">We offer Experience services with the best prices in town.</p>

    <footer class="contact">
      <div class="phone">Telephone: 0471932054</div>
      <div class="email">Email:marvtolk@quellnet.com</div>
    </footer>
  </main>
</body>
</html>
```